Business Card Design for my Real Estate Investing Company

This is for a Real Estate Investing Company that will be serving the Las Vegas Valley. Id like the following slogan included: "Investing in Our Community" I have attached my logo. You will see the color tones I'm interested in..in my logo. I would like the card to be double-sided with a modern, professional look.
Target Market(s)
Homeowners, banks, real estate industry
Industry/Entity Type
Real Estate
Contact Information for Business Card
name: Dale Pruitt
position: Managing Member
address: 4812 Corvane Pkwy ste 207-300
N. Las Vegas, NV 89517
phone: (702) 555-0143
fax: (702) 555-0187
email: OakridgeHousePurchaser@examplemail.com
web: OakridgeHousePurchasers.example
*At the bottom of the card I would like....
We buy houses for cash....no repairs, no commissions, no fees!
Logo Text
OAKRIDGE HOUSE PURCHASERS "Investing in Our Community"
Font styles to use
Other font styles liked:
- Lora
Requirements
Must have
- On the back of the card, i'd like to have my logo large and the following statements:
- Are you considering selling your home? Want a simple, hassle-free transaction? We can help! We buy houses for cash and can close quickly! No need to do any repairs, no realtor commissions, no closing costs.....and no headaches. Let us help you with your real estate needs...!
Nice to have
- multiple colors 2 two tone on front and back

```html
<!DOCTYPE html>
<html lang="en">
<head>
<meta charset="utf-8">
<title>Oakridge House Purchasers – Business Card</title>
<link rel="stylesheet" href="https://fonts.googleapis.com/css2?family=Questrial&display=swap">
<style>
  :root {
    --page: #ecebe8;
    --charcoal: #333333;
    --royal: #1f5fae;
    --white: #ffffff;
    --paper: #f4f4f4;
    --ink: #2b2b2b;
    --shadow: 0 6px 18px rgba(0,0,0,.18);
  }
  * { box-sizing: border-box; margin: 0; padding: 0; }
  html, body { width: 1200px; height: 1200px; overflow: hidden; }
  body {
    background: var(--page);
    font-family: "Questrial", "Century Gothic", sans-serif;
    position: relative;
  }
  .card {
    position: absolute;
    left: 172px;
    width: 850px;
    height: 488px;
    overflow: hidden;
    box-shadow: var(--shadow);
  }
  /* ---------- Front ---------- */
  .card-front { top: 107px; background: var(--royal); }
  .front-side {
    position: absolute; left: 0; top: 0; width: 350px; height: 488px;
    background: var(--charcoal);
  }
  .front-divider {
    position: absolute; left: 350px; top: 0; width: 6px; height: 488px;
    background: var(--white);
  }
  .icon-rail {
    position: absolute; left: 356px; top: 175px; width: 26px; height: 313px;
    background: var(--white);
  }
  .brand-band {
    position: absolute; left: 0; top: 175px; width: 350px; height: 150px;
    background: var(--white);
    display: flex; justify-content: center; align-items: center;
  }
  .wordmark {
    display: flex; align-items: center; gap: 14px;
  }
  .wordmark-square {
    flex: none; width: 22px; height: 22px; background: var(--royal);
  }
  .wordmark-name {
    color: var(--ink);
    font-size: 25px;
    line-height: 1.2;
  }
  .front-tagline {
    position: absolute; left: 0; top: 378px; width: 350px;
    color: var(--white); font-size: 15px; line-height: 23px; text-align: center;
  }
  .holder {
    position: absolute; left: 388px; top: 56px; color: var(--white);
  }
  .holder-name { font-size: 46px; line-height: 1; font-weight: 400; }
  .holder-role { font-size: 16px; margin: 14px 0 0 14px; }
  .contact-list { list-style: none; }
  .contact-item {
    position: absolute; left: 0; width: 850px; height: 30px;
  }
  .contact-icon {
    position: absolute; left: 360px; top: 4px; width: 18px; height: 18px;
  }
  .contact-text {
    position: absolute; left: 398px; top: 0;
    color: var(--white); font-size: 22px; line-height: 28px; white-space: nowrap;
  }
  .contact-text.is-long { font-size: 20px; }
  .contact-text.is-address { line-height: 26px; }
  /* ---------- Back ---------- */
  .card-back { top: 625px; background: var(--paper); }
  .back-tab {
    position: absolute; left: 280px; top: 0; width: 292px; height: 18px;
    background: var(--charcoal);
  }
  .back-brand {
    position: absolute; left: 0; top: 70px; width: 850px; height: 190px;
    display: flex; justify-content: center; align-items: center;
  }
  .back-brand .wordmark { gap: 20px; }
  .back-brand .wordmark-square { width: 36px; height: 36px; }
  .back-brand .wordmark-name { font-size: 46px; }
  .back-panel {
    position: absolute; left: 0; top: 315px; width: 850px; height: 173px;
    background: var(--royal);
    border-top: 8px solid var(--charcoal);
    padding: 16px 40px 0 40px;
    color: var(--white); font-size: 16.5px; line-height: 38px;
  }
  .back-panel p:first-child { padding-left: 6px; }
</style>
</head>
<body>

<section class="card card-front" aria-label="Business card front">
  <div class="front-side"></div>
  <div class="front-divider"></div>
  <div class="icon-rail"></div>

  <div class="brand-band">
    <div class="wordmark">
      <span class="wordmark-square" aria-hidden="true"></span>
      <span class="wordmark-name">Oakridge<br>House Purchasers</span>
    </div>
  </div>

  <p class="front-tagline">We buy houses for cash....no repairs,<br>no commissions, no fees!</p>

  <div class="holder">
    <h1 class="holder-name">Dale Pruitt</h1>
    <p class="holder-role">Managing member</p>
  </div>

  <ul class="contact-list">
    <li class="contact-item" style="top:180px">
      <svg class="contact-icon" viewBox="0 0 20 20" aria-hidden="true"><circle cx="10" cy="10" r="9" fill="none" stroke="#333" stroke-width="2"/><path d="M7 5.5l2 2.2-1 1.3c.7 1.4 1.7 2.4 3 3l1.3-1 2.2 2-1.2 1.5C9.8 14 6.4 10.6 5.5 7.2z" fill="#333"/></svg>
      <span class="contact-text">(702) 555-0143</span>
    </li>
    <li class="contact-item" style="top:228px">
      <svg class="contact-icon" viewBox="0 0 20 20" aria-hidden="true"><rect x="5" y="2" width="10" height="5" fill="#333"/><rect x="2" y="7" width="16" height="8" rx="1.5" fill="#333"/><rect x="5" y="12" width="10" height="6" fill="#fff" stroke="#333" stroke-width="1.6"/></svg>
      <span class="contact-text">(702) 555-0187</span>
    </li>
    <li class="contact-item" style="top:278px">
      <svg class="contact-icon" viewBox="0 0 20 20" aria-hidden="true"><circle cx="10" cy="10" r="9" fill="#333"/><path d="M5 7h10v7H5z" fill="none" stroke="#fff" stroke-width="1.3"/><path d="M5 7l5 4 5-4" fill="none" stroke="#fff" stroke-width="1.3"/></svg>
      <span class="contact-text is-long">OakridgeHousePurchaser@examplemail.com</span>
    </li>
    <li class="contact-item" style="top:326px">
      <svg class="contact-icon" viewBox="0 0 20 20" aria-hidden="true"><circle cx="10" cy="10" r="8" fill="none" stroke="#333" stroke-width="1.8"/><ellipse cx="10" cy="10" rx="3.5" ry="8" fill="none" stroke="#333" stroke-width="1.5"/><path d="M2 10h16M3.5 6h13M3.5 14h13" stroke="#333" stroke-width="1.3"/></svg>
      <span class="contact-text is-long">www.OakridgeHousePurchasers.example</span>
    </li>
    <li class="contact-item" style="top:374px">
      <svg class="contact-icon" viewBox="0 0 20 20" aria-hidden="true"><path d="M10 1.5c-3.6 0-6 2.6-6 6 0 4.3 6 11 6 11s6-6.7 6-11c0-3.4-2.4-6-6-6z" fill="none" stroke="#333" stroke-width="1.8"/><circle cx="10" cy="7.5" r="2.2" fill="#333"/></svg>
      <span class="contact-text is-address">4812 Corvane Pkwy ste 207-300<br>N. Las Vegas, NV 89517</span>
    </li>
  </ul>
</section>

<section class="card card-back" aria-label="Business card back">
  <div class="back-tab"></div>
  <div class="back-brand">
    <div class="wordmark">
      <span class="wordmark-square" aria-hidden="true"></span>
      <span class="wordmark-name">Oakridge House Purchasers</span>
    </div>
  </div>
  <div class="back-panel">
    <p>Are you considering selling your home? Want a simple, hassle-free transaction?</p>
    <p>We can help! We buy houses for cash and can close quickly! No need to do any repairs, no</p>
    <p>realtor commissions, no closing costs.....and no headaches. Let us help you with your real estate</p>
    <p>needs...!</p>
  </div>
</section>

</body>
</html>
```